Website for Hash Orbita a cyrpto Mining company that sells crypto mining rigs

β€œIn the age of de-centralised financial services, individuals with a relatively small investment can use their own hardware to process crypto transactions and earn a substantial second income.”

Hash Orbita provide a personal home and hosted mining solutions to enable individuals to earn monthly crypto currencies of today and the future.”
Home/Products/About
Images – I had assumed this was part of the Design? For the home page I have a 10 second video of blockchain. I can only find on Pixelvault For any text or sections please refer to our old website www.thirdheron.ae
https://www.pixelvaultmedia.com/video/clip-2947163058-block-chain-concept---consists-network-connections I can buy and send?
On each page I will have a video similar, can you just put placeholder images and videos. I can replace. I am pretty good with Wordpress.
Updates

Please use text from my old website www.thirdheronmining.com

Target Market(s)

High Net wealth interested in Crypto

Industry/Entity Type

Crypto Mining

Coding

Coded - Design and coding required

Number of Pages Required

5+ page

Font styles to use
Other font styles liked:
• Sansation

Colors
0054AA
0677BA
7BADD7
CADEEF
E8F1F8

Requirements
Must have
• Video as banner (Will supply Video), Wordpress
Nice to have
• Will need Member login and Shop in future, please ensure this will be possible. (But not part of this project)

```html
<!DOCTYPE html>
<html lang="en">
<head>
<meta charset="utf-8">
<title>Hash Orbita – About Us</title>
<link href="https://fonts.googleapis.com/css2?family=Exo+2:wght@300;400;500;600;700&family=Open+Sans:wght@400;600&display=swap" rel="stylesheet">
<style>
:root{
  --blue-deep:#0054AA;
  --blue:#0677BA;
  --blue-bright:#0a9be0;
  --blue-soft:#7BADD7;
  --cyan:#19f0f0;
  --ink:#000;
  --white:#fff;
  --muted:#e8f1f8;
  --field-text:#7d7d7d;
}
*{box-sizing:border-box;margin:0;padding:0}
html,body{width:1200px;height:3053px;overflow:hidden;background:var(--ink)}
body{position:relative;font-family:"Exo 2",sans-serif;color:var(--white)}

/* header */
.hero{position:absolute;left:0;top:0;width:1200px;height:672px}
.brand{position:absolute;left:100px;top:26px;display:flex;align-items:center;gap:12px;font-weight:500;font-size:28px;letter-spacing:2px;color:var(--blue-bright)}
.brand-dot{width:36px;height:36px;border-radius:50%;border:3px solid var(--blue-bright)}
.nav{position:absolute;top:33px;left:0;font-size:16px}
.nav a{position:absolute;color:var(--white);text-decoration:none;white-space:nowrap}
.login{position:absolute;left:970px;top:21px;width:129px;height:44px;background:var(--blue-bright);color:var(--white);font-size:16px;display:flex;align-items:center;justify-content:center;gap:6px;border-radius:2px}
.hero-title{position:absolute;top:468px;left:0;width:1200px;text-align:center;font-weight:400;font-size:66px;letter-spacing:1px}

/* about */
.about-photo{position:absolute;left:131px;top:772px;width:416px;height:416px}
.about-copy{position:absolute;left:659px;top:805px;width:442px}
.about-copy h2{font-weight:400;font-size:45px;letter-spacing:1px;line-height:1.1}
.about-lead{margin-top:20px;font-weight:600;font-size:16px;line-height:25px}
.about-body{margin-top:10px;font-size:14px;line-height:28px;text-align:justify;color:var(--white)}

/* team */
.team-title{position:absolute;top:1270px;left:0;width:1200px;text-align:center;font-weight:600;font-size:40px}
.team-title span{color:var(--blue-bright)}
.team-rule{position:absolute;left:557px;top:1331px;width:87px;height:3px;background:var(--blue-bright)}
.card{position:absolute;top:1396px;width:318px;height:334px;border:3px solid var(--blue)}
.card-photo{position:absolute;left:8px;top:8px;right:8px;bottom:8px}
.member{position:absolute;top:1741px;width:318px;text-align:center}
.member h3{font-weight:600;font-size:22px;line-height:28px}
.member p{margin-top:6px;font-family:"Open Sans",sans-serif;font-size:13px;line-height:18px;padding:0 22px}

/* contact */
.touch-band{position:absolute;left:0;top:1920px;width:1200px;height:720px}
.touch-title{position:absolute;top:2090px;left:0;width:1200px;text-align:center;font-weight:600;font-size:40px}
.field{position:absolute;background:var(--white);color:var(--field-text);font-family:"Open Sans",sans-serif;font-size:14px;padding:18px 18px}
.submit{position:absolute;left:505px;top:2431px;width:189px;height:44px;border:1.5px solid var(--white);border-radius:22px;display:flex;align-items:center;justify-content:center;font-family:"Open Sans",sans-serif;font-size:14px}

/* footer */
.foot-head{position:absolute;top:2733px;font-weight:600;font-size:17px}
.contact-item{position:absolute;left:142px;font-size:16px;line-height:21px;padding-left:38px}
.contact-item svg{position:absolute;left:4px;top:2px}
.quick{position:absolute;left:480px;top:2773px;list-style:none;font-size:16px;line-height:27.3px}
.news-input{position:absolute;left:693px;top:2786px;width:224px;height:45px;background:var(--white);color:var(--field-text);font-family:"Open Sans",sans-serif;font-size:13px;padding:14px 17px}
.news-btn{position:absolute;left:917px;top:2786px;width:138px;height:45px;background:var(--blue-bright);font-weight:700;font-size:16px;display:flex;align-items:center;justify-content:center}
.social{position:absolute;top:2862px;width:38px;height:38px;border:1.5px solid var(--blue-bright);border-radius:50%}
.copyright{position:absolute;top:3012px;left:0;width:1200px;text-align:center;font-size:16px}
</style>
</head>
<body>

<header class="hero">
  <svg width="1200" height="672" viewBox="0 0 1200 672" role="img" aria-label="Banner video: glowing circuit board with a floating crystal token">
    <defs>
      <linearGradient id="heroFill" x1="0" y1="0" x2="1" y2="1">
        <stop offset="0" stop-color="#1f3a3f"/>
        <stop offset="0.45" stop-color="#0f2a33"/>
        <stop offset="1" stop-color="#1d4b55"/>
      </linearGradient>
      <radialGradient id="heroGlow" cx="0.5" cy="0.4" r="0.4">
        <stop offset="0" stop-color="#2f8b95" stop-opacity="0.45"/>
        <stop offset="1" stop-color="#2f8b95" stop-opacity="0"/>
      </radialGradient>
    </defs>
    <path d="M0 0H1200V510L955 655Q943 662 930 658L599 575L295 658Q281 662 268 655L0 510Z" fill="url(#heroFill)"/>
    <path d="M0 0H1200V510L955 655Q943 662 930 658L599 575L295 658Q281 662 268 655L0 510Z" fill="url(#heroGlow)"/>
    <path d="M0 510L268 655Q281 662 295 658L599 575L930 658Q943 662 955 655L1200 510" fill="none" stroke="var(--blue-bright)" stroke-width="5"/>
  </svg>
  <div class="brand"><span class="brand-dot"></span>HASH ORBITA</div>
  <nav class="nav">
    <a style="left:495px">Home</a>
    <a style="left:569px">Services</a>
    <a style="left:659px">Product</a>
    <a style="left:745px">About</a>
    <a style="left:820px">FAQ</a>
    <a style="left:883px">Contact</a>
  </nav>
  <div class="login">
    <svg width="12" height="13" viewBox="0 0 12 13"><circle cx="6" cy="3.5" r="3" fill="#fff"/><path d="M0 13Q0 7 6 7Q12 7 12 13Z" fill="#fff"/></svg>
    LOGIN
  </div>
  <h1 class="hero-title">ABOUT US</h1>
</header>

<section>
  <svg class="about-photo" viewBox="0 0 416 416" role="img" aria-label="Photo of a businessman in glasses reading a tablet">
    <defs>
      <linearGradient id="aboutPhoto" x1="0" y1="0" x2="0" y2="1">
        <stop offset="0" stop-color="#cfd3d6"/>
        <stop offset="0.5" stop-color="#8aa3b8"/>
        <stop offset="1" stop-color="#4a5763"/>
      </linearGradient>
    </defs>
    <circle cx="208" cy="208" r="205" fill="none" stroke="#fff" stroke-width="5"/>
    <circle cx="208" cy="208" r="184" fill="url(#aboutPhoto)" stroke="var(--cyan)" stroke-width="6"/>
  </svg>
  <div class="about-copy">
    <h2>ABOUT HASH ORBITA</h2>
    <p class="about-lead">IT and Operations since 2000, Digital Payments since 2007, Crypto since 2012.</p>
    <p class="about-body">Marcus and Petar were part of the core team that built Zentrivo.com. Owen has been running IT and Operation teams of large companies for many years before setting up his own IT and Security Consultancy. Together this team know how to build, run and scale technology in Crypto and Payments, we only make 10% of your profits so we're dedicated to make your Third Heron mining rigs perform.</p>
  </div>
</section>

<section>
  <h2 class="team-title">MEET <span>OUR TEAM</span></h2>
  <div class="team-rule"></div>

  <div class="card" style="left:100px">
    <div class="card-photo" role="img" aria-label="Portrait of co-founder Marcus Hale at his desk" style="background:linear-gradient(160deg,#8d8a7e,#3a3a36 60%,#1c1c1c)"></div>
  </div>
  <div class="card" style="left:441px">
    <div class="card-photo" role="img" aria-label="Portrait of co-founder Owen Fairley in a white shirt" style="background:linear-gradient(180deg,#d9dcdc,#f2f2f2 60%,#e4e4e4)"></div>
  </div>
  <div class="card" style="left:781px">
    <div class="card-photo" role="img" aria-label="Photo of the technology and operations team reviewing data" style="background:linear-gradient(160deg,#b9bfc6,#4b5a70 55%,#1f2a3d)"></div>
  </div>

  <div class="member" style="left:100px">
    <h3>Marcus Hale</h3>
    <p>Co-Founder who operates the business licenses, accounts and financial service partnerships.</p>
  </div>
  <div class="member" style="left:438px">
    <h3>Owen Fairley</h3>
    <p>Co-Founder who designs, builds and maintains our hardware and software solutions.</p>
  </div>
  <div class="member" style="left:781px">
    <h3>Dimo &amp; Petar Koralov</h3>
    <p>Our Technology and Operations gurus who track the crypto markets daily. Their remote access to the Third Heron Mining</p>
  </div>
</section>

<section>
  <svg class="touch-band" viewBox="0 1920 1200 720" role="img" aria-label="Blue background with a faint hexagonal network mesh">
    <defs>
      <linearGradient id="touchFill" x1="0" y1="0" x2="0" y2="1">
        <stop offset="0" stop-color="#0a86c8"/>
        <stop offset="0.6" stop-color="#0a8fd2"/>
        <stop offset="1" stop-color="#0a7cc0"/>
      </linearGradient>
    </defs>
    <path d="M0 2075L268 1934Q281 1927 295 1931L599 2013L930 1931Q943 1927 955 1934L1200 2075V2485L955 2626Q943 2633 930 2629L599 2548L295 2629Q281 2633 268 2626L0 2485Z" fill="url(#touchFill)"/>
  </svg>
  <h2 class="touch-title">GET IN TOUCH</h2>
  <div class="field" style="left:267px;top:2163px;width:328px;height:54px">First Name</div>
  <div class="field" style="left:605px;top:2163px;width:328px;height:54px">Last Name</div>
  <div class="field" style="left:267px;top:2230px;width:328px;height:54px">Phone</div>
  <div class="field" style="left:605px;top:2230px;width:328px;height:54px">Email</div>
  <div class="field" style="left:267px;top:2296px;width:666px;height:115px">Message</div>
  <div class="submit">SUBMIT</div>
</section>

<footer>
  <h4 class="foot-head" style="left:142px">CONTACT US</h4>
  <h4 class="foot-head" style="left:477px">QUICK LINKS</h4>
  <h4 class="foot-head" style="left:694px">SIGN UP FOR NEWSLETTER</h4>

  <div class="contact-item" style="top:2786px">
    <svg width="16" height="20" viewBox="0 0 16 20"><path d="M8 0A8 8 0 0 0 0 8C0 14 8 20 8 20S16 14 16 8A8 8 0 0 0 8 0Z" fill="var(--blue-bright)"/><circle cx="8" cy="8" r="3" fill="#000"/></svg>
    Hash Orbita<br>195 enim ipsam<br>volatem quia voluptas
  </div>
  <div class="contact-item" style="top:2858px">
    <svg width="18" height="18" viewBox="0 0 18 18"><path d="M4 0L7 5L5 7Q7 11 11 13L13 11L18 14L16 18Q7 18 0 4Z" fill="var(--blue-bright)"/></svg>
    Phone:<br>808-5500 1200
  </div>
  <div class="contact-item" style="top:2910px">
    <svg width="18" height="14" viewBox="0 0 18 14" style="top:6px"><rect width="18" height="14" rx="2" fill="var(--blue-bright)"/><path d="M1 2L9 8L17 2" fill="none" stroke="#000" stroke-width="1.5"/></svg>
    Email:<br>info@hashorbita.ae
  </div>

  <ul class="quick">
    <li>Home</li><li>Services</li><li>&nbsp;Product</li><li>About</li><li>FAQ</li><li>Contact</li>
  </ul>

  <div class="news-input">Email *</div>
  <div class="news-btn">SUBMIT</div>

  <div class="social" style="left:866px" aria-label="Social profile link"></div>
  <div class="social" style="left:916px" aria-label="Social profile link"></div>
  <div class="social" style="left:965px" aria-label="Social profile link"></div>
  <div class="social" style="left:1015px" aria-label="Social profile link"></div>

  <p class="copyright">Hash Orbita© 2021 All Rights Reserved | Privacy Policy | Terms and Conditions</p>
</footer>

</body>
</html>
```